Book cover for book about Climate Change

Looking for a clean, bold, and attractive cover for a mass-market paperback (5.5"x 8.5") about solving the climate change problem. Title is either "When Rivers Learn to Sing” or A Lantern Over Quiet Fields” (your choice), subtitle is "A five-step plan to reverse climate change — to ensure that your grandchildren will live on a clean and comfortable planet," author is Dale Pruitt. Thinking that it *might* feature an image of Earth (or a portion thereof) and its very thin layer of atmosphere -- but STRONGLY encourage other ideas too!

Requirements
Nice to have
• Keep it positive — NOT scary doom-and-gloom

```html
<!DOCTYPE html>
<html lang="en">
<head>
<meta charset="utf-8">
<title>A Lantern Over Quiet Fields — Dale Pruitt</title>
<link href="https://fonts.googleapis.com/css2?family=Lato:wght@300;400;700;900&display=swap" rel="stylesheet">
<style>
  :root {
    --page-bg: #eef0f3;
    --space-deep: #050a1c;
    --space-mid: #0c1a3d;
    --horizon-glow: #f3a340;
    --horizon-warm: #ffd98a;
    --earth-blue: #1f6fb8;
    --earth-deep: #0a2f63;
    --ink-white: #ffffff;
  }
  * { box-sizing: border-box; margin: 0; padding: 0; }
  html, body {
    width: 862px;
    height: 1200px;
    overflow: hidden;
    background: var(--page-bg);
  }
  .stage {
    width: 862px;
    height: 1200px;
    display: flex;
    align-items: center;
    justify-content: center;
  }
  .book-cover {
    position: relative;
    width: 720px;
    height: 1112px;
    overflow: hidden;
    font-family: "Lato", sans-serif;
    color: var(--ink-white);
    box-shadow: 0 10px 30px rgba(0, 0, 0, 0.18);
  }
  .cover-art {
    position: absolute;
    inset: 0;
    background:
      radial-gradient(ellipse 140% 38% at 55% 66%, rgba(255, 217, 138, 0.85) 0%, rgba(243, 163, 64, 0.55) 14%, rgba(243, 163, 64, 0) 34%),
      radial-gradient(ellipse 120% 60% at 50% 100%, var(--earth-blue) 0%, #2a86cf 30%, var(--earth-deep) 62%, rgba(10, 47, 99, 0) 63%),
      linear-gradient(180deg, var(--space-deep) 0%, var(--space-mid) 45%, #1b2f5c 62%, var(--earth-deep) 100%);
  }
  .cover-content {
    position: relative;
    z-index: 1;
    height: 100%;
    padding: 70px 48px 0 48px;
  }
  .title-block {
    display: flex;
    flex-direction: column;
    align-items: flex-end;
  }
  .title-row-first {
    width: 100%;
    display: flex;
    justify-content: space-between;
    align-items: flex-start;
  }
  .author-name {
    font-weight: 400;
    font-size: 24px;
    letter-spacing: 0.42em;
    line-height: 1.55;
    text-transform: uppercase;
    padding-top: 6px;
    padding-left: 40px;
  }
  .book-title {
    font-weight: 900;
    font-size: 94px;
    line-height: 0.94;
    text-transform: uppercase;
    text-align: right;
    letter-spacing: -0.01em;
  }
  .book-title span { display: block; }
  .subtitle {
    position: absolute;
    left: 70px;
    right: 70px;
    top: 700px;
    text-align: center;
    font-weight: 400;
    font-size: 23px;
    line-height: 1.3;
    text-transform: uppercase;
    text-shadow: 0 1px 6px rgba(0, 0, 0, 0.45);
  }
  .subtitle strong { font-weight: 900; }
</style>
</head>
<body>
  <div class="stage">
    <article class="book-cover">
      <div class="cover-art" role="img" aria-label="Starry night sky above the curved horizon of Earth, with a glowing golden band of atmosphere and city lights over a blue planet"></div>
      <div class="cover-content">
        <header class="title-block">
          <div class="title-row-first">
            <p class="author-name">Dale<br>Pruitt</p>
            <h1 class="book-title"><span>A</span></h1>
          </div>
          <h1 class="book-title" aria-label="A Lantern Over Quiet Fields">
            <span>Lantern</span>
            <span>Over Quiet</span>
            <span>Fields</span>
          </h1>
        </header>
        <p class="subtitle"><strong>A five-step plan</strong> to reverse climate change — to ensure that your grandchildren will live on a clean and comfortable planet.</p>
      </div>
    </article>
  </div>
</body>
</html>
```